Cool modern, tech Business card design

Looking for a new business card design for our Managed IT Services company. We would like 2 sides, with the logo one one side horizontally and then the information on the back in either vertical or horizontal. We want our colors from the logo incorporated but also would like to see the color gray in there as well.

Target Market(s)

IT, Information Technology, Tech, Service

Industry/Entity Type

It Service

Contact Information for Business Card

Carl Penner
Managing Partner
(P)555-271-4830 ext xxx
(F)555-271-4831
www.brixtelcore.com

Font styles to use
Sans Serif

Colors
959595
000000
ec1f27

Requirements
Must have
• Logo on one side with some nice design or pattern
• Information on back in either vertical or horizontal format
Nice to have
• For it to look cool, tech, modern, stand out.

```html
<!DOCTYPE html>
<html lang="en">
<head>
<meta charset="utf-8">
<title>Brixtelcore Business Card</title>
<link href="https://fonts.googleapis.com/css2?family=Montserrat:ital,wght@0,500;0,600;0,800;1,700&display=swap" rel="stylesheet">
<style>
  :root {
    --brand-red: #ec1f27;
    --brand-black: #000000;
    --brand-gray: #959595;
    --card-white: #ffffff;
    --page-bg: #e4e4e6;
  }
  * { margin: 0; padding: 0; box-sizing: border-box; }
  html, body { width: 1200px; height: 1200px; overflow: hidden; }
  body {
    background: var(--page-bg);
    font-family: "Montserrat", Arial, sans-serif;
    position: relative;
  }
  .card {
    position: absolute;
    left: 220px;
    width: 760px;
    height: 440px;
    background: var(--card-white);
    box-shadow: 0 6px 18px rgba(0,0,0,0.18);
    overflow: hidden;
  }
  .card--front { top: 140px; }
  .card--back { top: 620px; }
  .card__art { position: absolute; inset: 0; width: 100%; height: 100%; }

  .wordmark {
    position: absolute;
    display: flex;
    align-items: center;
    gap: 14px;
    color: var(--brand-black);
    font-weight: 600;
    letter-spacing: -1px;
    white-space: nowrap;
  }
  .wordmark__mark { background: var(--brand-red); border-radius: 6px; }
  .card--front .wordmark {
    left: 0; right: 0; top: 180px;
    justify-content: center;
    font-size: 76px;
  }
  .card--front .wordmark__mark { width: 40px; height: 40px; }

  .holder {
    position: absolute;
    right: 60px;
    top: 48px;
    text-align: right;
  }
  .holder__name {
    font-weight: 800;
    font-size: 40px;
    letter-spacing: 1px;
    color: var(--brand-black);
    text-transform: uppercase;
  }
  .holder__rule {
    height: 4px;
    width: 340px;
    margin: 8px 0 8px auto;
    background: var(--brand-red);
  }
  .holder__title {
    font-weight: 700;
    font-style: italic;
    font-size: 23px;
    color: var(--brand-black);
  }

  .contacts {
    position: absolute;
    left: 66px;
    top: 222px;
    list-style: none;
  }
  .contacts__item {
    display: flex;
    align-items: center;
    gap: 14px;
    height: 56px;
    font-size: 25px;
    font-weight: 500;
    color: var(--brand-black);
  }
  .contacts__item--web { font-size: 21px; }
  .contacts__icon { width: 36px; height: 36px; flex: none; }

  .card--back .wordmark {
    right: 82px; bottom: 42px;
    font-size: 30px;
    gap: 8px;
    letter-spacing: -0.5px;
  }
  .card--back .wordmark__mark { width: 16px; height: 16px; border-radius: 3px; }
</style>
</head>
<body>

<section class="card card--front" aria-label="Card front">
  <svg class="card__art" viewBox="0 0 760 440" aria-hidden="true">
    <polygon points="0,95 95,0 165,0 0,165" fill="var(--brand-black)"/>
    <polygon points="0,195 195,0 260,0 0,260" fill="var(--brand-red)"/>
    <polygon points="0,290 290,0 305,0 0,305" fill="var(--brand-black)"/>
    <polygon points="760,150 760,215 535,440 470,440" fill="var(--brand-red)"/>
    <polygon points="760,245 760,260 580,440 565,440" fill="var(--brand-black)"/>
    <polygon points="760,300 760,440 620,440" fill="var(--brand-black)"/>
  </svg>
  <div class="wordmark"><span class="wordmark__mark"></span>brixtelcore</div>
</section>

<section class="card card--back" aria-label="Card back">
  <svg class="card__art" viewBox="0 0 760 440" aria-hidden="true">
    <polygon points="0,0 680,0 650,22 110,22 18,110 18,190 0,205" fill="var(--brand-red)"/>
    <polygon points="650,22 760,22 760,400 738,400 738,70 700,22" fill="var(--brand-black)"/>
    <polygon points="680,0 760,0 760,22 650,22" fill="var(--brand-black)"/>
    <polygon points="40,140 125,45 715,45 715,380 680,415 40,415" fill="none" stroke="var(--brand-gray)" stroke-width="2"/>
    <polygon points="0,330 18,315 18,420 230,420 210,440 0,440" fill="var(--brand-red)"/>
    <polygon points="520,440 738,400 760,400 760,440" fill="var(--brand-black)"/>
  </svg>

  <div class="holder">
    <div class="holder__name">Carl Penner</div>
    <div class="holder__rule"></div>
    <div class="holder__title">Managing Partner</div>
  </div>

  <ul class="contacts">
    <li class="contacts__item">
      <svg class="contacts__icon" viewBox="0 0 36 36" aria-hidden="true">
        <circle cx="18" cy="18" r="17" fill="var(--brand-red)"/>
        <path d="M12 9 l4 0 l2 5 l-3 2 q2 4 5 6 l2 -3 l5 2 l0 4 q-1 2 -4 2 q-13 -3 -13 -14 q0 -3 2 -4z" fill="#fff"/>
      </svg>
      (555) 271-4830
    </li>
    <li class="contacts__item">
      <svg class="contacts__icon" viewBox="0 0 36 36" aria-hidden="true">
        <circle cx="18" cy="18" r="17" fill="var(--brand-red)"/>
        <rect x="12" y="8" width="12" height="7" fill="#fff"/>
        <rect x="8" y="15" width="20" height="10" rx="2" fill="#fff"/>
        <rect x="12" y="22" width="12" height="6" fill="#fff" stroke="var(--brand-red)" stroke-width="1.5"/>
      </svg>
      (555) 271-4831
    </li>
    <li class="contacts__item contacts__item--web">
      <svg class="contacts__icon" viewBox="0 0 36 36" aria-hidden="true">
        <circle cx="18" cy="18" r="17" fill="var(--brand-red)"/>
        <circle cx="18" cy="18" r="9" fill="none" stroke="#fff" stroke-width="2"/>
        <ellipse cx="18" cy="18" rx="4" ry="9" fill="none" stroke="#fff" stroke-width="2"/>
        <line x1="9" y1="18" x2="27" y2="18" stroke="#fff" stroke-width="2"/>
      </svg>
      www.brixtelcore.com
    </li>
  </ul>

  <div class="wordmark"><span class="wordmark__mark"></span>brixtelcore</div>
</section>

</body>
</html>
```